energy rating company

Web Design graphics and layout only

To create two pages for the website. First the home page and the second is the design for the job board for our clients use after login. I have attached files that explain in detail what the pages should have and the purpose/desires of each object. Please read these thoroughly.

The webpages need to be clean, professional, easy on the eye, obvious in all its buttons and functions with a strong call to action on the home page and branding and clean, great and obvious looking buttons and very simple but dynamic as well. We wish to be seen as contemporary.

Business Concept

Our business concept is simple, to build a website whereby our clients will be able to upload jobs for energy raters to quote on and subsequent complete the work if their quote is selected. To link energy ratings that are required with energy raters via our website. Similarly to the varn website, jobs will be “advertised” on the job board and raters will select which jobs they wish to quote for.

I have attached a Word document explaining all the parts of the website and another word document showing what we are sort of after and a excel spreadsheet as well. Please read these in conjunction with this brief!
Updates

Dear All

I have submitted with my brief a word doc and excel spreadsheet of the two pages I want created.  However this is not the layout or design I want, I only put it together so that you will need to know what is required on each page.  Feel free to change and redesign it all.

Also the second page does not require the "process" logo or any other menu items except the first five being Home, How it works, About Us, testimonials and Contact us as per the home page.

We also are looking for something very professional and very clean.  It should be very easy to see exactly what you are looking for.

I will also extend the deadline for new designers!!  I am excited to see your talents!!

Thanks

I have increase budget and posted a note saying feel free to change all the details layout etc on my brief just include everything!!! 

Wanting a professional corporate look...

Want a professional corporate look

We have changed our minds and you we no longer require the process to be on the home page.

Thanks

Target Market(s)

Target Market

Home Inspection Companies
Pest Inspection Companies
Residential home buyers/sellers
Real Estate companies

Industry/Entity Type

It Company

Number of Pages Required

1 page

Requirements
Must have
• Colours and Styles

• The website should be mainly white as I believe it is seen as clean and simple with colour from the logos, but can be swayed if it projects the image we are after.

• It should be obvious and process orientated and I do believe symbols, pictures, etc should replace words where possible.

```html
<!DOCTYPE html>
<html lang="en">
<head>
<meta charset="utf-8">
<title>lumora australia – energy rating job board</title>
<link href="https://fonts.googleapis.com/css2?family=Arimo:wght@400;700&display=swap" rel="stylesheet">
<style>
:root{
  --orange:#c2561a;
  --orange-dark:#8a3410;
  --green:#4a9a2a;
  --green-light:#7cc04a;
  --lime:#9cbe0e;
  --red:#b80d0d;
  --teal:#a7c9c8;
  --grey-bg:#f2f2f2;
  --text:#333;
  --muted:#888;
  --line:#ddd;
}
*{box-sizing:border-box;margin:0;padding:0}
html,body{width:889px;height:1200px;overflow:hidden;background:var(--grey-bg)}
body{font-family:"Arimo",Arial,sans-serif;color:var(--text)}
.canvas{position:absolute;left:0;top:0;width:1260px;height:1700px;transform:scale(.7056);transform-origin:0 0;background:var(--grey-bg)}
.page{position:absolute;left:0;width:1260px}
.page-home{top:0}
.page-board{top:956px}

/* navigation */
.topnav{position:absolute;top:0;left:0;width:1260px;height:28px;background:linear-gradient(var(--green-light),var(--green));border-bottom:4px solid #d9d9d9}
.topnav ul{position:absolute;left:380px;top:0;display:flex;list-style:none}
.topnav li{height:28px;line-height:28px;color:#fff;font-size:12px;font-weight:700;text-align:center;border-right:1px solid #8fcf6a}
.topnav li.active{background:#dcdcdc;color:var(--orange)}
.topnav .account{position:absolute;left:970px;width:158px;height:28px;line-height:28px;background:#3f8e22;color:#e9e23a;font-size:11px;text-align:right;padding-right:12px}

.masthead{position:absolute;top:32px;left:0;width:1260px;height:90px;background:#fff;border-bottom:5px solid var(--orange)}
.brand{position:absolute;left:174px;top:20px;display:flex;align-items:center;gap:10px}
.brand-mark{width:56px;height:56px;border-radius:50%;background:#e7a21f}
.brand-name{font-size:36px;font-weight:700;color:var(--orange);letter-spacing:-.5px}
.cta{position:absolute;top:22px;width:182px;height:48px;border-radius:24px;background:linear-gradient(#fff,#eee);box-shadow:0 2px 4px rgba(0,0,0,.18);display:flex;align-items:center;gap:12px;padding-left:12px;font-weight:700;font-size:13px;color:var(--orange);letter-spacing:.3px}
.cta small{display:block;font-size:9px;font-weight:400;letter-spacing:0}
.cta-quote{left:462px}.cta-raters{left:672px}.cta-board{left:882px}
.cta svg{flex:none}

/* process band */
.process{position:absolute;top:127px;left:174px;width:912px;height:118px;background:var(--orange);border-radius:0 0 14px 14px;overflow:hidden}
.process svg.chev{position:absolute;top:0;left:0}
.step{position:absolute;top:0;height:118px;display:flex;align-items:center;gap:10px;color:#fff;font-size:12px;font-weight:700;line-height:14px}

/* cards */
.card{position:absolute;background:#fff;border-radius:8px;box-shadow:0 1px 3px rgba(0,0,0,.08)}
.card-title{font-size:12px;font-weight:700;color:var(--green);border-bottom:3px solid var(--orange);padding-bottom:2px;text-transform:uppercase;position:relative}
.card-title .more{position:absolute;right:0;bottom:3px;font-size:10px;font-weight:400;text-transform:none}

.intro{left:174px;top:263px;width:612px;height:593px;padding:18px 20px}
.intro h1{font-size:18px;line-height:21.5px;font-weight:700;color:#333}
.intro h1 .a{color:var(--orange)}.intro h1 .b{color:var(--green)}
.intro p{font-size:12px;color:var(--muted);line-height:14.5px;margin-top:14px}
.intro p.hl{color:var(--green);font-weight:700;margin-top:14px}
.benefits{list-style:none;border-top:1px solid var(--line);border-bottom:1px solid var(--line);margin-top:13px;padding:10px 0 12px 12px}
.benefits li{font-size:12px;font-weight:700;color:#444;height:29px;display:flex;align-items:center;gap:11px}

.login{left:799px;top:263px;width:287px;height:224px;padding:18px 22px}
.field{display:flex;align-items:center;margin-top:13px;font-size:12px;font-weight:700;color:var(--muted)}
.field span{width:72px}
.field i{display:block;width:171px;height:26px;border:1px solid #bbb;box-shadow:inset 0 1px 2px rgba(0,0,0,.1)}
.remember{margin:6px 0 0 72px;font-size:12px;color:var(--muted);display:flex;gap:6px;align-items:center}
.remember i{display:block;width:17px;height:17px;border:1px solid #bbb}
.btn-login{margin:8px 0 0 72px;width:82px;height:23px;background:var(--lime);color:#fff;font-size:12px;font-weight:700;text-align:center;line-height:23px;border-radius:2px}
.login .links{margin:10px 0 0 72px;color:var(--green);font-size:12px;font-weight:700;line-height:18px}

.testimonials{left:799px;top:502px;width:287px;height:355px;padding:18px 22px}
.quote{font-size:12px;line-height:14.5px;color:var(--orange);margin-top:18px;width:210px}
.who{margin-top:14px;font-size:12px;line-height:15px}
.who b{color:var(--green)}
.sep{width:210px;border-top:1px solid var(--line);margin-top:15px}

/* footer */
.footer{position:absolute;left:168px;width:700px;height:56px}
.footer .fbrand{position:absolute;left:0;top:12px;display:flex;align-items:center;gap:8px}
.footer .fbrand i{display:block;width:38px;height:38px;border-radius:50%;background:#aaa}
.footer .fbrand span{font-size:24px;font-weight:700;color:#777}
.footer .fnote{position:absolute;left:133px;top:0;height:56px;border-left:1px solid #ccc;padding:18px 0 0 12px;font-size:11px;color:var(--muted);line-height:16px}

/* board page */
.account-card{left:174px;top:144px;width:612px;height:242px;padding:20px 20px}
.details{width:573px;margin-top:12px;border-collapse:collapse;font-size:12px}
.details td{height:26px;border-bottom:1px solid #e6e6e6}
.details td:first-child{color:var(--muted);width:132px}
.details td:nth-child(2){color:var(--green)}
.details td:last-child{width:14px;text-align:right}
.details tr:last-child td{border-bottom:0}

.support{left:799px;top:144px;width:287px;height:242px;padding:20px 22px}
.agent{display:flex;align-items:center;gap:12px;margin-top:12px;font-size:12px;font-weight:700;color:var(--orange)}
.agent i{display:block;width:34px;height:34px;border-radius:50%;background:#35a8e0}
.agent.off i{background:#bfe3f4}
.support .links{border-top:1px solid var(--line);margin-top:10px;padding-top:10px;font-size:12px;font-weight:700;color:var(--green);line-height:18px}

.jobs{left:174px;top:398px;width:912px;height:242px;overflow:hidden}
.tabs{display:flex;height:46px}
.tab{width:304px;padding:23px 20px 0;background:linear-gradient(#e9e9e9,#f6f6f6)}
.tab.on{background:#fff}
.tab span{display:block;font-size:12px;font-weight:700;color:#ccc;border-bottom:3px solid #ddd;padding-bottom:1px}
.tab.on span{color:var(--green);border-color:var(--orange)}
.grid{margin:7px 0 0 20px;border-collapse:collapse;font-size:11px}
.grid th{height:33px;color:#aaa;font-weight:400;line-height:12px;border:1px solid #eee;text-transform:uppercase;font-size:11px}
.grid td{height:31px;border:1px solid #eee;font-weight:700;text-align:right;padding:0 8px}
.grid td.job{text-align:left;color:var(--orange)}
.grid td.c{text-align:center}
.grid td.act{text-align:left;padding:0 4px;border-right:0;white-space:nowrap}
.b{display:inline-block;height:22px;line-height:22px;color:#fff;font-size:12px;padding:0 5px;margin-right:1px}
.b-acc{background:var(--lime)}.b-deny{background:var(--red)}.b-mail{background:var(--teal);font-size:11px;font-weight:400}
</style>
</head>
<body>
<div class="canvas">

<!-- home page -->
<section class="page page-home">
  <nav class="topnav">
    <ul>
      <li class="active" style="width:78px">Home</li><li style="width:118px">How it works</li><li style="width:94px">About us</li><li style="width:120px">Testimonials</li><li style="width:75px">Help</li><li style="width:105px">Contact us</li>
    </ul>
    <div class="account">Login &nbsp;|&nbsp; Sign up</div>
  </nav>
  <header class="masthead">
    <div class="brand"><i class="brand-mark"></i><span class="brand-name">lumora</span></div>
    <div class="cta cta-quote"><svg width="38" height="38" viewBox="0 0 38 38"><circle cx="19" cy="19" r="18" fill="#5cae2e"/><path d="M10 15h18l-9 11z" fill="#fff"/></svg>GET A QUOTE</div>
    <div class="cta cta-raters"><svg width="38" height="38" viewBox="0 0 38 38"><path d="M14 3h10v11h11v10H24v11H14V24H3V14h11z" fill="#5cae2e"/></svg><div>ENERGY RATERS<small>ADD YOUR BUSINESS</small></div></div>
    <div class="cta cta-board"><svg width="30" height="30" viewBox="0 0 30 30"><path d="M3 16l8 8L27 6" stroke="#5cae2e" stroke-width="6" fill="none"/></svg>ACTIVE JOB BOARD</div>
  </header>

  <div class="process">
    <svg class="chev" width="912" height="118" viewBox="0 0 912 118">
      <g fill="#8e3a10" opacity=".75">
        <polygon points="88,0 116,0 176,59 116,118 88,118 148,59"/>
        <polygon points="312,0 340,0 400,59 340,118 312,118 372,59"/>
        <polygon points="530,0 558,0 618,59 558,118 530,118 590,59"/>
        <polygon points="690,0 718,0 778,59 718,118 690,118 750,59"/>
      </g>
    </svg>
    <div class="step" style="left:20px"><svg width="20" height="50" viewBox="0 0 20 50"><path d="M8 2h6l-1 36-3 10-3-10z" fill="#fff"/></svg>Post A Job</div>
    <div class="step" style="left:192px"><svg width="36" height="50" viewBox="0 0 36 50"><rect x="8" y="2" width="24" height="32" fill="#fff"/><rect x="2" y="8" width="24" height="32" fill="#eee" stroke="#8e3a10"/><path d="M10 40h8l-4 8z" fill="#fff"/></svg>Get<br>As Many Quotes<br>As You Like</div>
    <div class="step" style="left:418px"><svg width="38" height="38" viewBox="0 0 38 38"><rect x="2" y="2" width="34" height="34" fill="#fff"/><path d="M9 19l7 7 13-15" stroke="#c2561a" stroke-width="4" fill="none"/></svg>Select<br>Energy Quote<br>That Suits</div>
    <div class="step" style="left:624px"><svg width="42" height="42" viewBox="0 0 42 42"><circle cx="19" cy="23" r="17" fill="#fff"/><circle cx="19" cy="23" r="12" fill="#c2561a"/><text x="19" y="29" fill="#fff" font-size="16" font-weight="700" text-anchor="middle" font-family="Arimo">$</text><path d="M36 2v10M31 7h10" stroke="#fff" stroke-width="3"/></svg>Approve<br>Payment</div>
    <div class="step" style="left:790px"><svg width="40" height="42" viewBox="0 0 40 42"><rect x="2" y="2" width="26" height="26" fill="#fff"/><rect x="8" y="2" width="12" height="8" fill="#c2561a"/><path d="M22 18h14l-7 18z" fill="#c2561a" stroke="#fff" stroke-width="2"/></svg>Recieve<br>Rating</div>
  </div>

  <article class="card intro">
    <h1><span class="a">lumora</span> <span class="b">australia</span> is Australia’s leading professional energy rating consultancy firm specializing in large scaled residential and commercial energy rating logistics.</h1>
    <p>We have professional and accredited energy raters in all States and Territories ready and waiting to provide quotes for and perform your energy rating jobs!</p>
    <p class="hl">It’s Free, Fast and Easy to use and you get the best price and turnaround time that suits you!!</p>
    <p>Register with us, upload your job and specifications, and sit back and watch as energy raters provide quotes for your work!</p>
    <ul class="benefits">
      <li><svg width="14" height="12"><path d="M1 6l4 4 8-9" stroke="#5cae2e" stroke-width="3" fill="none"/></svg>Get the best priced quotes for your energy ratings</li>
      <li><svg width="14" height="12"><path d="M1 6l4 4 8-9" stroke="#5cae2e" stroke-width="3" fill="none"/></svg>Save time by listing a job to get many quotes</li>
      <li><svg width="14" height="12"><path d="M1 6l4 4 8-9" stroke="#5cae2e" stroke-width="3" fill="none"/></svg>Monitor your jobs and quotes on your own job board</li>
      <li><svg width="14" height="12"><path d="M1 6l4 4 8-9" stroke="#5cae2e" stroke-width="3" fill="none"/></svg>Be notified via email of all new quotes as they come in</li>
      <li><svg width="14" height="12"><path d="M1 6l4 4 8-9" stroke="#5cae2e" stroke-width="3" fill="none"/></svg>Be able to specify your desired turnaround times</li>
      <li><svg width="14" height="12"><path d="M1 6l4 4 8-9" stroke="#5cae2e" stroke-width="3" fill="none"/></svg>Accessible anytime and anywhere</li>
      <li><svg width="14" height="12"><path d="M1 6l4 4 8-9" stroke="#5cae2e" stroke-width="3" fill="none"/></svg>Choose a deadline for energy raters to supply quotes</li>
      <li><svg width="14" height="12"><path d="M1 6l4 4 8-9" stroke="#5cae2e" stroke-width="3" fill="none"/></svg>Have access to many qualified energy raters in your state all quoting for your work</li>
      <li><svg width="14" height="12"><path d="M1 6l4 4 8-9" stroke="#5cae2e" stroke-width="3" fill="none"/></svg>Be able to track your jobs and pay online</li>
      <li><svg width="14" height="12"><path d="M1 6l4 4 8-9" stroke="#5cae2e" stroke-width="3" fill="none"/></svg>Provide feedback on energy raters</li>
    </ul>
    <p style="margin-top:14px">Its totally free to be registered with us and there is no obligations or hidden catches! So if you wish to utilise the amazing opportunity register now! This new website will be going live on the (insert date) so be ready to save some money!</p>
  </article>

  <aside class="card login">
    <h2 class="card-title">Login</h2>
    <div class="field" style="margin-top:14px"><span>Username:</span><i></i></div>
    <div class="field" style="margin-top:10px"><span>Password:</span><i></i></div>
    <div class="remember"><i></i>Remember my password</div>
    <div class="btn-login">Login</div>
    <div class="links">Forgot your password?<br>Sign up!</div>
  </aside>

  <aside class="card testimonials">
    <h2 class="card-title">Testimonials<span class="more">more +</span></h2>
    <svg style="position:absolute;right:22px;top:43px" width="12" height="8"><path d="M0 8h12L6 0z" fill="#333"/></svg>
    <p class="quote">I'm very impressed with your service, I requested a quote for a new website and after answering your questions received the response from three companies who all new exactly what I was after saving me time and effort.</p>
    <p class="who"><b>Daniel Whitford</b><br>brightCast</p>
    <div class="sep"></div>
    <p class="quote" style="margin-top:16px">Les from Halden has already got in touch (just brilliant!) Thank you for thinking of me on the finance front. We will have to discuss this further. Thanks again.</p>
    <p class="who"><b>Marta Ilic</b><br>Director Civiform</p>
    <svg style="position:absolute;right:22px;bottom:17px" width="12" height="8"><path d="M0 0h12L6 8z" fill="#333"/></svg>
  </aside>

  <footer class="footer" style="top:885px">
    <div class="fbrand"><i></i><span>lumora</span></div>
    <div class="fnote">© 2010 lumora australia. All rights reserved.<br>Home &nbsp;|&nbsp; How it works &nbsp;|&nbsp; About us &nbsp;|&nbsp; Testimonials &nbsp;|&nbsp; Help &nbsp;|&nbsp; Contact us &nbsp;|&nbsp; Sitemap &nbsp;|&nbsp; Terms &amp; Conditions</div>
  </footer>
</section>

<!-- job board page -->
<section class="page page-board">
  <nav class="topnav">
    <ul>
      <li class="active" style="width:78px">Home</li><li style="width:118px">How it works</li><li style="width:94px">About us</li><li style="width:120px">Testimonials</li><li style="width:75px">Help</li><li style="width:105px">Contact us</li>
    </ul>
    <div class="account">Login &nbsp;|&nbsp; Sign up</div>
  </nav>
  <header class="masthead">
    <div class="brand"><i class="brand-mark"></i><span class="brand-name">lumora</span></div>
    <div class="cta cta-quote"><svg width="38" height="38" viewBox="0 0 38 38"><circle cx="19" cy="19" r="18" fill="#5cae2e"/><path d="M10 15h18l-9 11z" fill="#fff"/></svg>GET A QUOTE</div>
    <div class="cta cta-raters"><svg width="38" height="38" viewBox="0 0 38 38"><path d="M14 3h10v11h11v10H24v11H14V24H3V14h11z" fill="#5cae2e"/></svg><div>ENERGY RATERS<small>ADD YOUR BUSINESS</small></div></div>
    <div class="cta cta-board"><svg width="30" height="30" viewBox="0 0 30 30"><path d="M3 16l8 8L27 6" stroke="#5cae2e" stroke-width="6" fill="none"/></svg>ACTIVE JOB BOARD</div>
  </header>

  <section class="card account-card">
    <h2 class="card-title">My Account</h2>
    <table class="details">
      <tr><td>Company Details</td><td>Your Firm</td><td>✎</td></tr>
      <tr><td>Contact person</td><td>Sam Taylor</td><td>✎</td></tr>
      <tr><td>Email Address</td><td>sam@yourfirm.com</td><td>✎</td></tr>
      <tr><td>Sreet Adress</td><td>Level 1 - 212 Harbour Road</td><td>✎</td></tr>
      <tr><td>Suburb</td><td>Elmwood</td><td>✎</td></tr>
      <tr><td>State</td><td>VIC</td><td>✎</td></tr>
      <tr><td>Postcode</td><td>3120</td><td>✎</td></tr>
    </table>
  </section>

  <aside class="card support">
    <h2 class="card-title">Online Support</h2>
    <div class="agent" style="margin-top:14px"><i></i>Supporter 1</div>
    <div class="agent"><i></i>Supporter 2</div>
    <div class="agent off"><i></i>Supporter 3</div>
    <div class="links">FAQ<br>Email us</div>
  </aside>

  <section class="card jobs">
    <div class="tabs">
      <div class="tab on"><span>JOBS FOR QUOTING</span></div>
      <div class="tab"><span>ACTIVE JOBS</span></div>
      <div class="tab"><span>COMPLETED JOBS</span></div>
    </div>
    <table class="grid">
      <tr><th style="width:137px">Job</th><th style="width:84px">Quote<br>Number</th><th style="width:86px">Price</th><th style="width:84px">Total Price</th><th style="width:88px">Turnaround<br>Time</th><th style="width:86px">Rework<br>Price</th><th style="width:103px">Energy Raters<br>Accreditation</th><th style="width:212px;border-right:1px solid #eee"></th></tr>
      <tr><td class="job">Percy Place</td><td>111156</td><td>$250.00</td><td>$265.00</td><td class="c">5-10 days</td><td>$120</td><td class="c">VIC</td><td class="act"><span class="b b-acc">Accept</span><span class="b b-deny">Deny</span><span class="b b-mail">Email Energy Rater</span></td></tr>
      <tr><td class="job">Royal Place</td><td>111156</td><td>$250.00</td><td>$265.00</td><td class="c">5-10 days</td><td>$120</td><td class="c">QLD</td><td class="act"><span class="b b-acc">Accept</span><span class="b b-deny">Deny</span><span class="b b-mail">Email Energy Rater</span></td></tr>
      <tr><td class="job">Nottingham Place</td><td>111156</td><td>$250.00</td><td>$265.00</td><td class="c">5-10 days</td><td>$120</td><td class="c">SA</td><td class="act"><span class="b b-acc">Accept</span><span class="b b-deny">Deny</span><span class="b b-mail">Email Energy Rater</span></td></tr>
      <tr><td class="job">Dublin Place</td><td>111156</td><td>$250.00</td><td>$265.00</td><td class="c">5-10 days</td><td>$120</td><td class="c">QLD</td><td class="act"><span class="b b-acc">Accept</span><span class="b b-deny">Deny</span><span class="b b-mail">Email Energy Rater</span></td></tr>
    </table>
  </section>

  <footer class="footer" style="top:666px">
    <div class="fbrand"><i></i><span>lumora</span></div>
    <div class="fnote">© 2010 lumora australia. All rights reserved.<br>Home &nbsp;|&nbsp; How it works &nbsp;|&nbsp; About us &nbsp;|&nbsp; Testimonials &nbsp;|&nbsp; Help &nbsp;|&nbsp; Contact us &nbsp;|&nbsp; Sitemap &nbsp;|&nbsp; Terms &amp; Conditions</div>
  </footer>
</section>

</div>
</body>
</html>
```